Domestic Violence Consulting Firm needs double sided page flyer

We need a flyer for an upcoming Juvenile Justice conference in Florida that addresses a form of domestic violence called child to parent violence or parent abuse. This is when an adolescent is aggressive, abusive and violent toward a parent or caregiver and is arrested for Domestic Violence. The child attends Lantern Bridge Family Program with their parent who is the victim. We would like to see traditional DV photos but a with a new twist of the parent being the victim. The final design should promote shock to this new subject of domestic violence and interest to our program that addresses this subject. You can get more information about this at www.homefrontmendwork.com
Updates

REVISED CONTENT WITH A CALL TO ACTION Who we are: The silent suffering of parents abused by their adolescent is a serious and often hidden issue within families. Adolescent to Parent Abuse, internationally known as Child to Parent Violence is a complex family and public health problem. Stories from parents who are willing to speak about their abuse reveal the pain of victims who must by law care for their abuser. Abuse by teens in the home feels extremely violating as a youth steps out of their place in the natural family hierarchy. Understandably so, parents are often exhausted, carry deep grief as victims, feel shock and become isolated in shame and blame with nowhere to turn for understanding or help. Parents are not alone in their frustration and confusion associated with how to address Child to Parent Violence. Juvenile Justice Judges, State District Attorneys, Probation Officers, Child Welfare Case Managers and Law Enforcement Officers are often frustrated by who to turn to for professional services to intervene in this silent epidemic. Therefore, Lantern Bridge Consulting offers an array of consultative, collaborative and experienced professional services to a variety of clientele affected by Child to Parent Violence. Our specialized approach takes into account the serious ongoing need for safety of each family member. We have extensive experience with the nuances of this particular family and community challenge and offer a haven of safety to address this highly stigmatized topic. What we do: Lantern Bridge Family Program (bold) is conducted in a unique group setting within the juvenile justice probation and diversion program where families significantly reduce abuse and violence within the home. Parents and youth work together with trained facilitators through ten highly relational, psycho-educational sessions. Youth face their behaviors with weekly accountability and without minimizing, justifying or denying their disrespectful and abusive acts. Lantern Bridge Family Coaching (bold) is a private option for parents that encourages exploration of each family's values and individuality and facilitates discovery of their own personalized parenting style that respects the uniqueness of each family member and acknowledges the special history of each family unit. Lantern Bridge Training (bold) offers customized live and e-learning seminars, presentations, webinars and continued educational trainings for organizations. We are nationally recognized trainers in Adult and Youth Steady Minds Basics and Harbor Growth Outline Scheme (HGOS). Train the trainer course for the Lantern Bridge Family Program is available upon request. Why we are the experts: We recognize that the relationship between a parent-child has a distinctiveness unlike those of intimate partners and requires a different approach. We address the societal concerns and needs of public safety, by providing youth with necessary and supportive accountability for their abuse behaviors through our Lantern Bridge Family Program. We honor each family’s culture, acknowledges the trauma of parenting a teen with abusive behaviors, nurtures each family’s strengths, and empowers all families to identify their individual needs. We motivate individuals, families and community with a focus on the global and basic human need for safety. We, the program designers, are recognized as subject matter experts on the topic and present at numerous local, state and national venues. We offer private consultative, collaborative and experienced professional services to agencies, communities and parents. Contact us today: facebook, website, twitter, linkedin (Call to action)

REVISED CONTENT FOR DOUBLE SIDED FLYER The silent suffering of parents abused by their adolescent is a serious and often hidden issue within families. Adolescent to Parent Abuse, internationally known as Child to Parent Violence is a complex family and public health problem. Stories from parents who are willing to speak about their abuse reveal the pain of victims who must by law care for their abuser. Abuse by teens in the home feels extremely violating as a youth steps out of their place in the natural family hierarchy and behaves with a squad of disrespectful and intense behaviors. Understandably so, parents are often exhausted, carry deep grief as victims, feel shock at experiencing their child’s abuse, and become isolated in shame and blame with nowhere to turn for understanding or help. Parents are not alone in their frustration and confusion associated with how to address Child to Parent Violence. Juvenile Justice Judges, State District Attorneys, Probation Officers, Child Welfare Case Managers and Law Enforcement Officers are often frustrated by who to turn to for professional services to intervene in this silent epidemic. Therefore, Lantern Bridge Consulting (bold) offers an array of consultative, collaborative and experienced professional services to a variety of clientele affected by Child to Parent Violence. Our specialized approach takes into account the serious ongoing need for safety of each family member. We have extensive experience with the nuances of this particular family and community challenge and offer a haven of safety to address this highly stigmatized topic. What we offer: Lantern Bridge Family Program (bold) is conducted in a unique group setting within the juvenile justice probation and diversion program where families significantly reduce abuse and violence within the home. Parents and youth work together with trained facilitators through ten highly relational, psycho-educational sessions. Youth face their behaviors with weekly accountability and without minimizing, justifying or denying their disrespectful and abusive acts. Lantern Bridge Family Coaching (bold) is a private option for parents that encourages exploration of each family's values and individuality and facilitates discovery of their own personalized parenting style that respects the uniqueness of each family member and acknowledges the special history of each family unit. Lantern Bridge Training (bold) offers customized live and e-learning seminars, webinars and continued educational trainings for organizations. We are nationally recognized trainers in Adult and Youth Steady Minds Basics and Harbor Growth Outline Scheme (HGOS). Train the trainer course for the Lantern Bridge Family Program is available. How we are different: We recognize that the relationship between a parent-child has a distinctiveness unlike those of intimate partners that require a different approach. We address the societal concerns and needs of public safety, by providing youth with necessary and supportive accountability for their abuse behaviors. We honor each family’s culture, acknowledges the trauma of parenting a teen with abusive behaviors, nurturing each family’s strengths, and empower all families to identify their individual needs. We motivate individuals, families and communities with a focus on the global and basic human need for safety. We, the program designers, are recognized as subject matter experts on the topic and have presented at numerous local, state and national venues. We offer private consultative, collaborative and experienced professional services to agencies, communities and parents. Lets talk, contact us today to help your community address Child to Parent Violence (facebook, linkedin, website and twitter)

Target Market(s)

Department of Juvenile Justice, Law Enforcement, State Attorney, Probation Officers, Child Welfare Agency, Department of Child and Family, Legislators and Parents

Industry/Entity Type

Consulting

Font styles to use
Serif

Requirements
Must have
• Colorful, professional and double sided flyer with imagery similar to domestic violence but with an adolescent as the batterer towards the parent/caregiver. Description of how Lantern Bridge Consulting provides a evidenced promised 10 week community based program designed to reduce teen abuse and violence within the home. And consulting services such as train the trainer for the program, presentations, parent coaching and independent educational consulting services to parents.
Nice to have
• OCR for the website

```html
<!DOCTYPE html>
<html lang="en">
<head>
<meta charset="utf-8">
<title>Lantern Bridge Family Program Flyer</title>
<link href="https://fonts.googleapis.com/css2?family=Lato:wght@400;700;900&family=Teko:wght@500&family=Merriweather:ital,wght@0,700;1,700&display=swap" rel="stylesheet">
<style>
  :root {
    --backdrop: #4a4a4c;
    --blue: #1f5c9e;
    --blue-deep: #134379;
    --blue-light: #2f78c0;
    --orange: #e0401c;
    --gold: #f3c21a;
    --band-text: #f4b537;
    --ink: #2b2b2b;
    --paper: #ffffff;
  }
  * { box-sizing: border-box; margin: 0; padding: 0; }
  html, body { width: 1200px; height: 846px; overflow: hidden; }
  body { background: var(--backdrop); font-family: "Lato", Arial, sans-serif; position: relative; }

  .page { position: absolute; top: 52px; width: 518px; height: 670px; background: var(--paper); overflow: hidden; }
  .page--front { left: 60px; }
  .page--back { left: 601px; }

  /* FRONT */
  .hero-photo { position: absolute; left: 0; top: 0; width: 518px; height: 258px;
    background: linear-gradient(180deg, #7fc4ec 0%, #b7dcf1 45%, #e8c3a2 75%, #c89a76 100%); }
  .brand-box { position: absolute; left: 132px; top: 198px; width: 264px; height: 60px;
    background: rgba(255,255,255,0.9); display: flex; align-items: center; gap: 8px; padding: 0 8px; }
  .brand-mark { width: 48px; height: 48px; border-radius: 50%; background: #e39a2a; flex: none; }
  .brand-name { font-family: "Merriweather", Georgia, serif; font-weight: 700; font-size: 10.5px; color: #222; line-height: 1.2; }
  .brand-tag { font-family: "Merriweather", Georgia, serif; font-style: italic; font-weight: 700; font-size: 7.5px; color: #222; line-height: 1.3; margin-top: 3px; }
  .brand-tag b { color: var(--orange); }

  .intro-band { position: absolute; left: 0; top: 258px; width: 518px; height: 162px;
    background: linear-gradient(180deg, var(--blue-light), var(--blue)); border-bottom: 3px solid var(--orange); }
  .intro-text { position: absolute; left: 16px; top: 5px; width: 492px; color: var(--band-text);
    font-size: 7.2px; line-height: 1.27; }
  .intro-gap { float: right; width: 84px; height: 118px; margin-top: 18px; margin-left: 4px;
    shape-outside: ellipse(50% 50%); }
  .intro-text p + p { margin-top: 2px; }
  .intro-photo { position: absolute; left: 428px; top: 24px; width: 104px; height: 112px; border-radius: 50%;
    border: 4px solid var(--orange); background: radial-gradient(circle at 45% 45%, #b9aa9a, #6c625a); }

  .columns { position: absolute; left: 14px; top: 428px; width: 492px; display: flex; gap: 14px;
    font-size: 7.6px; line-height: 1.22; color: var(--ink); text-align: justify; hyphens: auto; }
  .columns .col { flex: 1; }
  .columns p + p { margin-top: 7px; }
  .lead { color: var(--orange); font-weight: 700; text-transform: uppercase; }

  .contact-box { position: absolute; left: 30px; width: 458px; height: 66px; border-radius: 10px;
    background: var(--orange); color: #fff; font-weight: 700; font-size: 14px; line-height: 1.3;
    text-align: center; display: flex; flex-direction: column; justify-content: center; }
  .page--front .contact-box { top: 597px; }

  /* BACK */
  .back-top { position: absolute; left: 0; top: 0; width: 518px; height: 463px;
    background: linear-gradient(180deg, var(--blue-deep) 0%, var(--blue) 55%, var(--blue-light) 100%); }
  .back-title { position: absolute; left: 9px; top: 16px; width: 262px; font-family: "Teko", "Arial Narrow", sans-serif;
    font-weight: 500; font-size: 29px; line-height: 1.05; color: #fff; text-transform: uppercase; white-space: nowrap; }
  .back-sub { position: absolute; left: 9px; top: 100px; width: 238px; color: var(--gold); font-size: 17.5px; line-height: 1.28; }
  .feature-ring { position: absolute; left: 257px; top: -70px; width: 330px; height: 330px; border-radius: 50%;
    background: var(--orange); }
  .feature-photo { position: absolute; left: 270px; top: -62px; width: 318px; height: 318px; border-radius: 50%;
    border: 5px solid #fff; background: radial-gradient(circle at 50% 55%, #e88c45 0%, #cfb89c 45%, #d8cbb9 100%); }

  .bullets { position: absolute; list-style: none; color: #fff; font-size: 9.4px; line-height: 1.3; }
  .bullets li { position: relative; padding-left: 10px; }
  .bullets li::before { content: ""; position: absolute; left: 0; top: 3px; border-left: 6px solid var(--orange);
    border-top: 3.5px solid transparent; border-bottom: 3.5px solid transparent; }
  .bullets--left { left: 9px; top: 202px; width: 238px; }
  .bullets--right { left: 278px; top: 279px; width: 232px; text-align: justify; }

  .kids-photo { position: absolute; left: 0; top: 463px; width: 518px; height: 207px;
    background: linear-gradient(180deg, #9fc6e4 0%, #d9a77a 40%, #f0c54a 65%, #6ea84a 100%); }
  .page--back .contact-box { top: 593px; left: 31px; width: 456px; }
</style>
</head>
<body>

<section class="page page--front">
  <div class="hero-photo" role="img" aria-label="Photo of smiling children leaning into the camera under a blue sky"></div>
  <div class="brand-box">
    <div class="brand-mark"></div>
    <div>
      <div class="brand-name">Lantern Bridge Consulting, Inc.</div>
      <div class="brand-tag"><b>HOPE</b> for families experiencing teen abuse and violence within the home.</div>
    </div>
  </div>

  <div class="intro-band">
    <div class="intro-text">
      <div class="intro-gap"></div>
      <p>The silent topic of teen abuse and violence toward a parent or guardian is an all too common family secret requiring an understanding that is different from traditional domestic violence theories. Utilizing a replicable, innovative collaboration model that incorporates the Family Health Services Network (FHSN) System of Care (SOC) guiding principles and values, Lantern Bridge Family Program (LBF) currently implements psycho-educational groups within the juvenile justice probation and diversion program where families significantly reduce abuse and violence within the home. LBF is an emerging curriculum including attention to progression from research, to pilot, to scale.</p>
      <p>Stories from parents who are willing to speak about their abuse reveal the pain of victims who must by law care for their abuser. The escalation of a youth's feelings and behaviors into a pattern of abusive behaviors is often met with disbelief on the part of the victim and family unit. Uncertainty exists among the parents on what is 'normal' for teens in today's culture, and they often wonder if the abuse is a passing phase like so many other phases of child and human development. Abuse by teens in the home feels extremely violating as a youth steps out of their place in the natural family hierarchy and behaves with a cadre of disrespectful and intense behaviors. Understandably so, parents are often exhausted, carry deep grief as victims, feel shock at experiencing their child's abusive lashing out, and become isolated in shame and blame with nowhere to turn for understanding or help.</p>
    </div>
    <div class="intro-photo" role="img" aria-label="Photo of a child sitting alone hugging their knees"></div>
  </div>

  <div class="columns">
    <div class="col">
      <p><span class="lead">Lantern Bridge Family Program</span> is conducted in a unique group setting. Through ten highly relational, psycho-educational sessions, parents and youth work together with other families. Families are greatly encouraged when they discover they are not alone in the journey of abuse. LBF honors each family's culture, acknowledges the trauma of parenting a teen with abusive behaviors, nurtures each family's strengths, and empowers all families to identify their individual needs. LBF provides a supportive and safe place for families to explore and make changes pertinent to their situation.</p>
      <p><span class="lead">Lantern Bridge Family Program</span> provides both parents and youth the time to grow together in their understanding of abuse. Together they acquire a variety of skills and concepts that strengthen them in this challenging area of life. LBF acknowledges parents as experts in their own families.</p>
    </div>
    <div class="col">
      <p>Youth face their behaviors with accountability and without minimizing, justifying or denying their disrespectful and abusive actions. Participants forge the bonds of familial respect as they face their struggles of disrespect, abuse and violence. Together, parents and youth create shared goals for improving respect and decreasing abuse.</p>
      <p><span class="lead">Lantern Bridge Family Program</span> groups offer a respite of civility, personal growth, and encouragement during the storms of family life. LBF addresses the societal concerns and needs of public safety, provides youth with necessary and supportive accountability for their abuse, and builds competency in developmentally appropriate social and emotional skills needed by teens to replace their abusive and violent behaviors. It is true; hope and healing are possible for families that have been ravaged and devastated by teen abuse and violence.</p>
    </div>
  </div>

  <div class="contact-box">
    <span>www.homefrontmendwork.com</span>
    <span>https://www.friendspage.net/LBconsulting</span>
    <span>https://www.chirpline.net/homefront_help</span>
  </div>
</section>

<section class="page page--back">
  <div class="back-top"></div>
  <div class="feature-ring"></div>
  <div class="feature-photo" role="img" aria-label="Photo of a young boy in an orange shirt sitting alone on the ground"></div>
  <h1 class="back-title">What makes Lantern<br>Bridge Family Program</h1>
  <p class="back-sub">So effective at reducing teen abuse and violence in the home?</p>

  <ul class="bullets bullets--left">
    <li>We understand that traditional domestic violence battery interventions, concepts, and philosophies for adult intimate partner abuse is not developmentally appropriate for adolescents and traditional approaches result in an increase of teen abuse and violence within the home.</li>
    <li>We recognize that the relationship between a parent-child has a distinctiveness unlike those of intimate partners.</li>
    <li>We motivate attendees with a focus on the global and basic human need for safety.</li>
    <li>We provide a relationship based positive peer setting where teens are weekly accountable in a group setting for their behaviors toward parents.</li>
    <li>We emphasis on safety combined with the parent component serves as a highly protective factor for the contagion challenge typical in delinquent settings.</li>
    <li>We facilitate a safe, open, and non-judgmental environment where family units of any culture can work together as a parent child team to address the abusive behaviors that are particular to their home.</li>
  </ul>

  <ul class="bullets bullets--right">
    <li>We deliver lessons that target key concepts and universally recognized communication skills to address behaviors and the underlying emotions that developed into a domestic violence charge.</li>
    <li>We incorporate the Family Health Services Network (FHSN) System of Care Principles and Values.</li>
    <li>We, the program designers, are recognized as subject matter experts on the topic and have presented at numerous state and national venues.</li>
    <li>We understand the complex nuances of this form of domestic violence having served over 150 teens charged with Domestic Violence or Battery against a caregiver with a total of over 200 individuals including parents or other caregivers.</li>
  </ul>

  <div class="kids-photo" role="img" aria-label="Photo of smiling children lying together on the grass"></div>

  <div class="contact-box">
    <span>www.homefrontmendwork.com</span>
    <span>https://www.friendspage.net/LBconsulting</span>
    <span>https://www.chirpline.net/homefront_help</span>
  </div>
</section>

</body>
</html>
```